Business Card Design

we are a brand new cable TV network devoted to self improvement and leading a better life called FLOURIVO TV.I have a logo. We have 3 executives that need cards.I want it to be a heavy stock card: professional but showing our creative nature

Industry/Entity Type

Business

Contact Information for Business Card

CLAUDIA SAENZ AMLIECEO350 San Juan DrPonte Vedra Beach FL 32082904-473-5953

```html
<!DOCTYPE html>
<html lang="en">
<head>
<meta charset="utf-8">
<title>Flourivo TV Business Card</title>
<link rel="stylesheet" href="https://fonts.googleapis.com/css2?family=Source+Sans+3:wght@400;600;800&display=swap">
<style>
  :root {
    --page-bg: #ecebe8;
    --brand-red: #c8202a;
    --brand-red-deep: #9b2430;
    --brand-red-bright: #d41f27;
    --card-white: #ffffff;
    --ink: #2a2a2a;
    --ink-soft: #3d3d3d;
    --card-shadow: rgba(0, 0, 0, 0.18);
  }
  * { box-sizing: border-box; margin: 0; padding: 0; }
  html, body {
    width: 1200px;
    height: 900px;
    overflow: hidden;
    background: var(--page-bg);
    font-family: "Source Sans 3", "Myriad Pro", Arial, sans-serif;
  }
  .canvas {
    position: relative;
    width: 1200px;
    height: 900px;
  }
  .card {
    position: absolute;
    left: 320px;
    width: 560px;
    height: 320px;
    border-radius: 3px;
    box-shadow: 0 8px 24px var(--card-shadow);
    overflow: hidden;
  }
  .card--front {
    top: 100px;
    background: linear-gradient(180deg, var(--brand-red-deep) 0%, var(--brand-red-bright) 100%);
    display: flex;
    align-items: center;
    justify-content: center;
  }
  .card--back {
    top: 480px;
    background: var(--card-white);
  }
  .wordmark {
    font-weight: 800;
    letter-spacing: 0.5px;
    white-space: nowrap;
  }
  .card--front .wordmark {
    color: var(--card-white);
    font-size: 58px;
  }
  .card--back .wordmark {
    position: absolute;
    left: 36px;
    bottom: 34px;
    color: var(--brand-red);
    font-size: 36px;
  }
  .contact {
    position: absolute;
    left: 318px;
    top: 30px;
    color: var(--ink);
  }
  .contact__name {
    color: var(--brand-red);
    font-weight: 600;
    font-size: 17px;
    letter-spacing: 0.2px;
  }
  .contact__title {
    font-size: 13px;
    margin-top: 3px;
    color: var(--ink-soft);
  }
  .contact__phone {
    display: flex;
    align-items: center;
    gap: 6px;
    font-size: 13px;
    margin-top: 16px;
  }
  .contact__phone svg { width: 11px; height: 11px; fill: var(--brand-red); }
  .contact__address {
    font-style: normal;
    font-size: 13px;
    line-height: 1.45;
    margin-top: 14px;
    margin-left: 17px;
  }
</style>
</head>
<body>
  <main class="canvas">
    <section class="card card--front" aria-label="Card front">
      <p class="wordmark">FLOURIVO TV</p>
    </section>

    <section class="card card--back" aria-label="Card back">
      <div class="contact">
        <h1 class="contact__name">Mirella Okafor Dunst</h1>
        <p class="contact__title">CEO</p>
        <p class="contact__phone">
          <svg viewBox="0 0 24 24" aria-hidden="true"><path d="M6.6 10.8a15.2 15.2 0 0 0 6.6 6.6l2.2-2.2c.3-.3.7-.4 1-.2 1.1.4 2.3.6 3.6.6.6 0 1 .4 1 1V20c0 .6-.4 1-1 1A17 17 0 0 1 3 4c0-.6.4-1 1-1h3.5c.6 0 1 .4 1 1 0 1.3.2 2.5.6 3.6.1.3 0 .7-.2 1z"/></svg>
          904-618-2047
        </p>
        <address class="contact__address">
          718 Harlow Creek Dr<br>
          Ponte Vedra Beach FL 32097
        </address>
      </div>
      <p class="wordmark">FLOURIVO TV</p>
    </section>
  </main>
</body>
</html>
```